Real estate company needs a letterhead design

A young real estate company needs a letterhead / stationery design, it should include the company's logo. It should look exactly the same as on the business cards. (With the phrase "a brand of KEV Wohnbau & Grundstücksentwicklung GmbH")

In addition, it should also include the 4 round seals.

color code blue # 00456b gray # 333333

Word and PDF are welcome.

KEV Wohnbau & Grundstücksentwicklung GmbH
Managing director: Mag. Lukas Fellnhuber
Matthias-Ortner-Strasse 3c / 41
6300 Wörgl

Tel .: +436648172093
Email: office@wohnglanz-beispiel.at
Web: www.wohnglanz-beispiel.at

Sparkasse Almtal, Bergländer Sparkasse from 1882, Genossenschaftskasse
Anton-Weissauer-Strasse 7, 6300 Wörgl
IBAN: AT31 4817 2964 0058 2316
BIC: GLMTAT44XXX
Account holder: KEV Wohnbau & Grundstücksentwicklung GmbH

FN: XXXXXXX
UID: XXXXXXX

```html
<!DOCTYPE html>
<html lang="en">
<head>
<meta charset="utf-8">
<title>Letterhead</title>
<link href="https://fonts.googleapis.com/css2?family=Lato:wght@400;700;900&family=Open+Sans:wght@400&display=swap" rel="stylesheet">
<style>
  :root {
    --brand-blue: #00456b;
    --navy: #1c2a55;
    --text-grey: #333333;
    --body-grey: #555555;
    --seal-red: #e8402a;
    --paper: #ffffff;
  }
  * { margin: 0; padding: 0; box-sizing: border-box; }
  html, body { width: 1040px; height: 1200px; overflow: hidden; background: var(--paper); }
  .letterhead {
    position: relative; width: 1040px; height: 1200px; background: var(--paper);
    font-family: "Open Sans", sans-serif; color: var(--body-grey);
  }
  .brand { position: absolute; left: 99px; top: 48px; }
  .brand-name {
    display: flex; align-items: center; gap: 10px;
    font-family: "Lato", sans-serif; font-weight: 900; font-size: 44px;
    letter-spacing: 0.5px; color: var(--brand-blue); line-height: 1;
  }
  .brand-mark { width: 14px; height: 14px; background: var(--brand-blue); }
  .brand-tagline {
    margin-top: 14px; font-family: "Lato", sans-serif; font-size: 13.5px; color: var(--text-grey);
  }
  .contact-divider { position: absolute; left: 630px; top: 30px; width: 1px; height: 148px; background: #cccccc; }
  .contact { position: absolute; left: 650px; top: 32px; font-family: "Lato", sans-serif; font-style: normal; color: var(--text-grey); }
  .contact-name { font-weight: 700; font-size: 18px; color: var(--brand-blue); }
  .contact-role { font-size: 16px; margin-top: 1px; }
  .contact-list { list-style: none; margin-top: 10px; font-size: 16px; line-height: 21px; }
  .contact-list li { display: flex; align-items: center; gap: 7px; }
  .contact-list svg { width: 14px; height: 14px; flex: none; }
  .contact-address { margin-top: 9px; font-size: 16px; line-height: 20px; }
  .rule { position: absolute; left: 105px; width: 822px; height: 3px; background: var(--navy); }
  .rule-top { top: 200px; }
  .rule-bottom { top: 1083px; background: #222222; }
  .letter { position: absolute; left: 99px; top: 216px; width: 839px; font-size: 15px; }
  .issue-date { margin-bottom: 17px; }
  .recipient { line-height: 18px; margin-bottom: 50px; }
  .salutation { margin-bottom: 26px; }
  .body-text p {
    font-size: 16.5px; text-align: justify; hyphens: auto;
    line-height: 27px; margin-bottom: 27px;
  }
  .closing { margin-top: 50px; }
  .signer { font-size: 19px; color: var(--text-grey); margin: 4px 0 6px; }
  .seals { position: absolute; top: 990px; left: 0; width: 100%; display: flex; justify-content: center; gap: 14px; }
  .seal { width: 86px; height: 86px; border-radius: 50%; border: 2px solid var(--seal-red); padding: 9px; }
  .seal span { display: block; width: 100%; height: 100%; border-radius: 50%; background: var(--seal-red); }
  .footer { position: absolute; top: 1100px; font-family: "Lato", sans-serif; font-size: 16px; color: #111111; line-height: 20px; }
  .footer-bank { left: 120px; }
  .footer-bank .bank-detail { margin-top: 4px; color: var(--text-grey); }
  .footer-register { left: 791px; top: 1122px; }
</style>
</head>
<body>
<main class="letterhead">
  <header>
    <div class="brand">
      <div class="brand-name"><span>WOHNGLANZ</span><span class="brand-mark"></span></div>
      <p class="brand-tagline">A brand of KEV Wohnbau &amp; Grundstücksentwicklung GmbH</p>
    </div>
    <div class="contact-divider"></div>
    <address class="contact">
      <div class="contact-name">MAG. LUKAS FELLNHUBER</div>
      <div class="contact-role">Managing Director</div>
      <ul class="contact-list">
        <li><svg viewBox="0 0 14 14"><rect width="14" height="14" rx="3" fill="#1c2a55"/><path d="M4 3.5l1.6 0 .7 2-1 .8c.6 1.2 1.4 2 2.6 2.6l.8-1 2 .7v1.6c-4 .4-7.1-2.7-6.7-6.7z" fill="#fff"/></svg>+436648172093</li>
        <li><svg viewBox="0 0 14 14"><rect width="14" height="14" rx="3" fill="#1c2a55"/><rect x="3" y="4" width="8" height="6" fill="none" stroke="#fff" stroke-width="1.2"/><path d="M3 4l4 3.5L11 4" fill="none" stroke="#fff" stroke-width="1.2"/></svg>office@wohnglanz-beispiel.at</li>
        <li><svg viewBox="0 0 14 14"><circle cx="7" cy="7" r="7" fill="#1c2a55"/><circle cx="7" cy="7" r="4" fill="none" stroke="#fff" stroke-width="1"/><path d="M3 7h8M7 3v8" stroke="#fff" stroke-width="1"/></svg>www.wohnglanz-beispiel.at</li>
      </ul>
      <div class="contact-address">Matthias-Ortner-Strasse 3c / 41<br>6300 Wörgl</div>
    </address>
  </header>
  <div class="rule rule-top"></div>

  <article class="letter">
    <p class="issue-date">Issuing Date: May 5, 2018</p>
    <p class="recipient">Name Of Employee Mr. XYZABC<br>Address of Employee<br>Address Line 2 etc..</p>
    <p class="salutation">Dear Mr.XYZABC</p>
    <div class="body-text">
      <p>Lorem Ipsum has been the industry's standard dummy text ever since the 1500s, when an unknown printer took a galley of type and scrambled it to make a type specimen book. It has survived not only five centuries, but also the leap into electronic typesetting, remaining essentially unchanged. It was popularised in the 1960s with the release of Typoflex sheets containing Lorem Ipsum passages, and more recently with desktop publishing software like Folio LayoutDesk including versions of Lorem Ipsum.</p>
      <p>Lorem Ipsum is simply dummy text of the printing and typesetting industry. Lorem Ipsum has been the industry's standard dummy text ever since the 1500s, when an unknown printer took a galley of type and scrambled it to make a type specimen book.</p>
      <p>It has survived not only five centuries, but also the leap into electronic typesetting, remaining essentially unchanged. It was popularised in the 1960s with the release of Typoflex sheets containing Lorem IpsumIpsum passages.</p>
    </div>
    <div class="closing">
      <p>Yours Sincerely</p>
      <p class="signer">Jonas Berger</p>
      <p>Managing Director</p>
    </div>
  </article>

  <div class="seals">
    <div class="seal" role="img" aria-label="Certification seal"><span></span></div>
    <div class="seal" role="img" aria-label="Certification seal"><span></span></div>
    <div class="seal" role="img" aria-label="Certification seal"><span></span></div>
    <div class="seal" role="img" aria-label="Certification seal"><span></span></div>
  </div>
  <div class="rule rule-bottom"></div>

  <footer>
    <div class="footer footer-bank">
      <div>IBAN: AT31 4817 2964 0058 2316 | BIC: GLMTAT44XXX</div>
      <div>Account holder: KEV Wohnbau &amp; Grundstücksentwicklung GmbH</div>
      <div class="bank-detail">Sparkasse Almtal, Bergländer Sparkasse from 1882, Genossenschaftskasse<br>Anton-Weissauer-Strasse 7, 6300 Wörgl</div>
    </div>
    <div class="footer footer-register">FN: XXXXXXX<br>UID: XXXXXXX</div>
  </footer>
</main>
</body>
</html>
```